Redesign of Current Wix Website - Event Production Company

Our website is www.trulvanshows.com and we need a redesign. We are full service event production company offering clients services including event management, graphics and content creation, vendor sourcing and management, contract review, audio visual production and venue selection. We would like our website to look more like an event management company, not just an audio visual company which it looks like now.
We want to look more like www.basquirelabs.com
Our Wix account is FILLED with logos, pictures and all the graphics you will need and we can assist with assets, categories and text.
On the Logo, I want to move away from "TRV Shows" and move to "Halvindor Stage Production" and I would like a redesigned logo with the same center element but a name change. I do have the art work files for the logo, vector and ai.

Target Market(s)

Event Planners and people that book event services. Assistants of CEOs. Marketing Directors. Gala Chairpersons and people in positions to purchase large scale event production

Industry/Entity Type

Event Management and Production - Corporate and Social

Coding

Coded - Design and coding required

Font styles to use
Other font styles liked:
• my logo is multicolor. look at it before you design

Colors
0054AA
0677BA
7BADD7
CADEEF
E8F1F8
6B429C
8869AF
B7A5CE
E3DAEB
F3F0F8

Requirements
Must have
• A clean professional look that shows the client who we are and what we do, and the full scope of what we do.
Nice to have
• www.basquirelabs.com ; https://themarbledrift.com/ look at these two website We are going after venues, planners end clients. Much like the on service page.

```html
<!DOCTYPE html>
<html lang="en">
<head>
<meta charset="UTF-8">
<title>Halvindor Stage Production</title>
<link href="https://fonts.googleapis.com/css2?family=Montserrat:wght@600;700;800&family=Lato:wght@400;700&display=swap" rel="stylesheet">
<style>
:root{
  --blue:#1f6db5;
  --blue-deep:#0054aa;
  --band:#2b72b4;
  --pale:#e8edf5;
  --ink:#111111;
  --text:#333333;
  --muted:#555555;
  --white:#ffffff;
  --footer:#121212;
}
*{margin:0;padding:0;box-sizing:border-box}
html,body{width:1200px;height:3863px;overflow:hidden}
body{font-family:'Lato',sans-serif;color:var(--text);background:var(--white);position:relative}
.abs{position:absolute}
.btn{position:absolute;display:flex;align-items:center;justify-content:center;background:var(--blue);color:var(--white);font-family:'Lato',sans-serif;font-weight:700;font-size:15px;border-radius:22px;text-decoration:none}
h2.section-title{position:absolute;left:0;width:1200px;text-align:center;font-family:'Montserrat',sans-serif;font-weight:700;font-size:40px;color:var(--ink)}
h2.section-title span{color:var(--blue)}

/* hero */
.hero{position:absolute;left:0;top:0;width:1200px;height:677px;background:radial-gradient(ellipse at 50% 20%,#4a56b8 0%,#2a2f86 40%,#14163f 80%,#0b0c22 100%)}
.brand-mark{position:absolute;left:163px;top:33px;width:110px;height:110px;border-radius:50%;background:#1a1a1a;border:3px solid #e6e6e6}
.brand-name{position:absolute;left:90px;top:150px;width:256px;text-align:center;color:var(--white);font-family:'Lato',sans-serif;font-size:22px;line-height:25px;letter-spacing:.3px}
.main-nav{position:absolute;top:37px;left:400px;display:flex;align-items:center;font-size:15px;color:var(--white)}
.main-nav a{color:var(--white);text-decoration:none;margin-right:39px}
.main-nav a.active{background:var(--blue);padding:10px 16px;border-radius:20px;margin-right:24px}
.quote-top{left:934px;top:34px;width:153px;height:42px;font-size:16px}
.hero-title{position:absolute;top:272px;left:0;width:1200px;text-align:center;color:var(--white);font-family:'Montserrat',sans-serif;font-weight:800;font-size:54px;line-height:68px;letter-spacing:.5px}
.hero-sub{position:absolute;top:420px;left:0;width:1200px;text-align:center;color:var(--white);font-size:20px;line-height:27px}
.hero-cta{left:509px;top:502px;width:182px;height:42px}
.dots{position:absolute;left:0;width:1200px;display:flex;justify-content:center;gap:8px}
.dots i{width:12px;height:12px;border-radius:50%;background:#555a7a;display:block}
.dots i.on{background:var(--white)}

/* services */
.intro{position:absolute;top:816px;left:170px;width:860px;text-align:center;font-size:18px;line-height:26px;color:var(--text)}
.card-photo{position:absolute;width:309px;height:239px}
.card-title{position:absolute;width:309px;text-align:center;font-family:'Montserrat',sans-serif;font-weight:600;font-size:18px;color:var(--ink)}
.card-text{position:absolute;width:309px;text-align:center;font-size:14px;line-height:24px;color:var(--muted);padding:0 18px}
.arrow{position:absolute;width:37px;height:37px;border-radius:50%;background:var(--blue)}

/* about */
.about-bg{position:absolute;left:0;top:1430px;width:643px;height:600px;background:var(--pale)}
.about-photo{position:absolute;left:643px;top:1430px;width:557px;height:600px;background:linear-gradient(135deg,#3a3530 0%,#1c1a18 45%,#2d3b4a 75%,#151515 100%)}
.about-title{position:absolute;left:110px;top:1510px;font-family:'Montserrat',sans-serif;font-weight:700;font-size:40px;color:var(--ink)}
.about-title span{color:var(--blue)}
.about-copy{position:absolute;left:111px;top:1584px;width:470px;font-size:16px;line-height:25.5px;color:var(--text)}
.about-copy p+p{margin-top:25px}

/* cta band */
.cta-band{position:absolute;left:0;top:2030px;width:1200px;height:353px;background:var(--band)}
.cta-title{position:absolute;top:2098px;left:0;width:1200px;text-align:center;font-family:'Montserrat',sans-serif;font-weight:700;font-size:40px;color:var(--white)}
.cta-text{position:absolute;top:2164px;left:185px;width:830px;text-align:center;font-size:18px;line-height:26px;color:var(--white)}
.cta-btn{left:523px;top:2264px;width:154px;height:41px;background:var(--ink)}

/* footer */
.footer{position:absolute;left:0;top:3322px;width:1200px;height:541px;background:var(--footer)}
.video{position:absolute;left:111px;top:3089px;width:978px;height:372px;background:linear-gradient(90deg,#3c4048 0%,#5b5e63 40%,#6e7176 60%,#4b4f55 100%)}
.play{position:absolute;left:568px;top:3243px;width:64px;height:64px}
.f-head{position:absolute;top:3536px;font-family:'Lato',sans-serif;font-weight:700;font-size:21px;color:var(--white)}
.f-text{position:absolute;font-size:14px;line-height:25.5px;color:#e6e6e6}
.f-list{position:absolute;list-style:none;font-size:14px;color:#e6e6e6}
.f-list li{height:43px}
.social{position:absolute;top:3714px;left:113px;display:flex;gap:14px}
.social i{display:block;width:30px;height:30px;border-radius:4px;border:2px solid #e6e6e6}
.social i.on{background:var(--blue);border-color:var(--blue);width:38px;height:38px;margin-top:-4px}
.f-rule{position:absolute;left:111px;top:3820px;width:978px;height:1px;background:#3a3a3a}
.copyright{position:absolute;top:3835px;left:0;width:1200px;text-align:center;font-size:12px;color:#dddddd}
.contact-row{position:absolute;left:470px;display:flex;gap:22px;font-size:14px;line-height:25.5px;color:#e6e6e6}
.contact-row svg{flex:none;margin-top:4px}
</style>
</head>
<body>

<header class="hero" role="img" aria-label="Concert stage with moving-head lights and blue light beams">
</header>
<div class="brand-mark" aria-hidden="true"></div>
<div class="brand-name">HALVINDOR STAGE<br>PRODUCTION</div>
<nav class="main-nav">
  <a class="active" href="#">Home</a>
  <a href="#">About Us</a>
  <a href="#">Services</a>
  <a href="#">HSP Social Media</a>
  <a href="#">Contact</a>
</nav>
<a class="btn quote-top" href="#">Get A Quote</a>
<h1 class="hero-title">TRANSFORMING IDEAS<br>INTO EXTRAORDINARY EVENTS</h1>
<p class="hero-sub">Where creativity meets precision to bring your vision to life with<br>unforgettable experiences.</p>
<a class="btn hero-cta" href="#">Let’s Get Started</a>
<div class="dots" style="top:610px"><i class="on"></i><i></i><i></i><i></i></div>

<!-- Services -->
<h2 class="section-title" style="top:755px">Our <span>Services</span></h2>
<p class="intro">At Halvindor Stage Production, we specialize in delivering seamless, innovative, and impactful events. Whether you’re planning a corporate conference, a gala dinner, or a private celebration, our comprehensive services are designed to bring your vision to life.</p>

<svg class="arrow" style="left:54px;top:1024px" viewBox="0 0 37 37"><circle cx="18.5" cy="18.5" r="18.5" fill="#1f6db5"/><path d="M21 11.5 14 18.5 21 25.5" fill="none" stroke="#fff" stroke-width="3" stroke-linecap="round" stroke-linejoin="round"/></svg>
<svg class="arrow" style="left:1108px;top:1024px" viewBox="0 0 37 37"><circle cx="18.5" cy="18.5" r="18.5" fill="#1f6db5"/><path d="M16 11.5 23 18.5 16 25.5" fill="none" stroke="#fff" stroke-width="3" stroke-linecap="round" stroke-linejoin="round"/></svg>

<div class="card-photo" style="left:111px;top:918px;background:linear-gradient(160deg,#7a4a32,#3a2a22 60%,#1e1a18)" role="img" aria-label="Technicians running an event control desk in a brick venue"></div>
<div class="card-title" style="left:111px;top:1173px">Event Management</div>
<p class="card-text" style="left:111px;top:1207px">Lorem ipsum dolor sit amet, consectetur adipiscing elit, sed do eiusmod tempor incididunt ut labore et dolore aliqua.</p>
<a class="btn" style="left:189px;top:1302px;width:154px;height:42px" href="#">Read More</a>

<div class="card-photo" style="left:446px;top:918px;background:linear-gradient(160deg,#1d3a44,#0f1f26 60%,#0a1216)" role="img" aria-label="Hand holding glowing digital media icons"></div>
<div class="card-title" style="left:446px;top:1173px">Graphics &amp; Content Creation</div>
<p class="card-text" style="left:446px;top:1207px">Lorem ipsum dolor sit amet, consectetur adipiscing elit, sed do eiusmod tempor incididunt ut labore et dolore aliqua.</p>
<a class="btn" style="left:523px;top:1302px;width:154px;height:42px" href="#">Read More</a>

<div class="card-photo" style="left:780px;top:918px;background:linear-gradient(160deg,#5a6070,#2b2e36 55%,#1a1b20)" role="img" aria-label="Audio visual mixing console with monitors"></div>
<div class="card-title" style="left:780px;top:1173px">Audio Visual Production</div>
<p class="card-text" style="left:780px;top:1207px">Lorem ipsum dolor sit amet, consectetur adipiscing elit, sed do eiusmod tempor incididunt ut labore et dolore aliqua.</p>
<a class="btn" style="left:858px;top:1302px;width:154px;height:42px" href="#">Read More</a>

<!-- About -->
<div class="about-bg"></div>
<div class="about-photo" role="img" aria-label="Music production studio with computer, speakers and keyboard"></div>
<h2 class="about-title">About <span>Us</span></h2>
<div class="about-copy">
  <p>As an Event Producer with over 25 years of national event production experience, I partner with a diverse client base and a network of vendor partners to deliver complete production bids on a range of services from audio visual to drape and lighting.</p>
  <p>&nbsp;I own and operate TRV Shows LLC, a company that provides event production and event technology services for Corporate, Social and Non-profit clients. I specialize in Event Technologies, advising on strategies to best create, capture, and broadcast your message, meeting, or story.</p>
</div>
<a class="btn" style="left:111px;top:1900px;width:154px;height:42px" href="#">Read More</a>

<!-- CTA -->
<section class="cta-band"></section>
<h2 class="cta-title">Let’s Bring Your Event to Life!</h2>
<p class="cta-text">Ready to create an unforgettable experience? Our team is here to provide you with a tailored quote based on your unique event needs. Whether you’re planning a small gathering or a large-scale production, we’ll guide you every step of the way to ensure your vision is realized.</p>
<a class="btn cta-btn" href="#">Get A Quote</a>

<!-- Social -->
<h2 class="section-title" style="top:2460px">HSP Social <span>Media</span></h2>

<div class="card-photo" style="left:111px;top:2536px;background:linear-gradient(160deg,#5b4a3e,#2a221d 60%,#15110e)" role="img" aria-label="Plated dinner served at an event"></div>
<p class="card-text" style="left:111px;top:2796px">Halvindor Stage Production has a big week! I’m #downtownliving this week while we work at Corvane Hall Denton excited to partner with VELMAR 2024</p>
<a class="btn" style="left:188px;top:2914px;width:154px;height:42px" href="#">Read More</a>

<div class="card-photo" style="left:446px;top:2536px;background:linear-gradient(160deg,#8a6a4a,#4a3a2e 55%,#2a221c)" role="img" aria-label="Guests at banquet tables during a morning event"></div>
<p class="card-text" style="left:446px;top:2796px">Amazing morning ! providing the audiovisual production for Ridgefold Chamber at Tamsworth Grill House!</p>
<a class="btn" style="left:523px;top:2914px;width:154px;height:42px" href="#">Read More</a>

<div class="card-photo" style="left:780px;top:2536px;background:linear-gradient(180deg,#9ec3e6 0%,#c8d6df 45%,#6f7a5c 75%,#8a8a80 100%)" role="img" aria-label="Festival dancers in costume in front of a domed building"></div>
<p class="card-text" style="left:780px;top:2796px">The Denton Ledger-Courier put out a BEAUTIFUL article about the return of the Denton Harvest Festival! We are going back to a traditional festival ..</p>
<a class="btn" style="left:857px;top:2914px;width:154px;height:42px" href="#">Read More</a>

<div class="dots" style="top:2990px"><i class="on" style="background:#1f6db5"></i><i style="background:#9a9a9a"></i><i style="background:#9a9a9a"></i><i style="background:#9a9a9a"></i></div>

<!-- Footer -->
<footer class="footer"></footer>
<div class="video" role="img" aria-label="Video still of a speaker in a modern office"></div>
<svg class="play" viewBox="0 0 64 64"><circle cx="32" cy="32" r="32" fill="#1f6db5"/><path d="M26 20 44 32 26 44Z" fill="#fff"/></svg>

<h3 class="f-head" style="left:114px">About Us</h3>
<p class="f-text" style="left:112px;top:3584px;width:290px">I own and operate TRV Shows LLC, a company that provides event production and event technology services for Corporate, Social and Non-profit clients.</p>
<div class="social"><i class="on"></i><i></i><i></i></div>

<h3 class="f-head" style="left:470px">Contact Us</h3>
<div class="contact-row" style="top:3586px">
  <svg width="18" height="20" viewBox="0 0 18 20"><path d="M9 1a6.5 6.5 0 0 0-6.5 6.5C2.5 12 9 19 9 19s6.5-7 6.5-11.5A6.5 6.5 0 0 0 9 1Z" fill="none" stroke="#e6e6e6" stroke-width="1.5"/><circle cx="9" cy="7.5" r="2.2" fill="none" stroke="#e6e6e6" stroke-width="1.5"/></svg>
  <span>48 Lantern Row Suite 12,<br>Stage District 10482.</span>
</div>
<div class="contact-row" style="top:3660px">
  <svg width="18" height="18" viewBox="0 0 18 18"><path d="M4 1.5 7 5 5.5 7a9 9 0 0 0 5.5 5.5L13 11l3.5 3-1.5 2.5C9 16.5 1.5 9 1.5 3Z" fill="none" stroke="#e6e6e6" stroke-width="1.5" stroke-linejoin="round"/></svg>
  <span>(555) 014-2270</span>
</div>
<div class="contact-row" style="top:3714px">
  <svg width="18" height="14" viewBox="0 0 18 14"><rect x="1" y="1" width="16" height="12" rx="1.5" fill="none" stroke="#e6e6e6" stroke-width="1.5"/><path d="M1.5 2 9 8l7.5-6" fill="none" stroke="#e6e6e6" stroke-width="1.5"/></svg>
  <span>hello@halvindorstage.com</span>
</div>

<h3 class="f-head" style="left:765px">Quick Links</h3>
<ul class="f-list" style="left:766px;top:3591px"><li>Home</li><li>About Us</li><li>Services</li><li>HSP Social Media</li></ul>

<h3 class="f-head" style="left:975px">Other Links</h3>
<ul class="f-list" style="left:978px;top:3591px"><li>Get In Touch</li><li>Contact</li><li>Privacy Policy</li><li>Terms of Service</li></ul>

<div class="f-rule"></div>
<p class="copyright">Copyright © 2025 Event Production Company. All rights reserved.</p>

</body>
</html>
```